Sun Keel (www.sunkeel.com) web site development

Sun Keel is a new Fishing, Spearfishing Charter operator offering private charters in North Belize, Turneffe, Lighthouse Reef and the Blue Hole. The logo of the company has been designed by Pixelvane, some months ago. We have also developed a small brochure which can be the base for the website development (at least colors, fonts, etc.).
Pictures and Video should be an important asset of this website. We need to be able to update contents (video, photos), update prices and destinations, etc.

Target Market(s)

High hand, fishing and spearfishing enthusiasts.

Industry/Entity Type

Yacht charter

Coding

Coded - Design and coding required

Number of Pages Required

4 page

Colors
EB3D1F
EC4F4E
F09395
F8D3D4
FCEDEE

Requirements
Must have
• Optimized for phone and tablet navigation, must be easy to update with photos and video, connected to our Instagram and Shoalbook page,

```html
<!DOCTYPE html>
<html lang="en">
<head>
<meta charset="utf-8">
<title>Sun Keel – Private Fishing, Spearfishing &amp; Snorkeling Charters</title>
<link href="https://fonts.googleapis.com/css2?family=Exo+2:ital,wght@1,800&family=Rubik:wght@400;500&display=swap" rel="stylesheet">
<style>
:root{
  --red:#e4132f;
  --ink:#1b1b1b;
  --text:#3a3a3a;
  --navy:#173a4d;
  --pink:#fce8ea;
  --white:#ffffff;
  --black:#050505;
  --sea-deep:#1e4f8f;
  --sea-light:#6fa6d6;
}
*{box-sizing:border-box;margin:0;padding:0}
html,body{width:1200px;height:3934px;overflow:hidden}
body{font-family:"Rubik",sans-serif;color:var(--text);background:var(--white);position:relative}
.heading{font-family:"Exo 2",sans-serif;font-style:italic;font-weight:800;text-transform:uppercase;color:var(--ink);letter-spacing:-.5px}
.btn{display:inline-block;background:var(--red);color:var(--white);font-weight:500;text-transform:uppercase;text-decoration:none;text-align:center}
.btn-lg{font-size:15px;padding:13px 18px;letter-spacing:.3px}
.btn-sm{font-size:12px;padding:9px 14px}
.photo{display:block}

/* header */
.site-header{position:absolute;top:0;left:0;width:1200px;height:125px}
.brand{position:absolute;left:130px;top:34px;display:flex;align-items:center;gap:10px;font-family:"Rubik",sans-serif;font-weight:500;font-size:30px;color:var(--navy)}
.brand-dot{width:26px;height:26px;border-radius:50%;background:var(--red)}
.contact-bar{position:absolute;top:22px;right:132px;display:flex;gap:40px}
.contact-item{display:flex;align-items:center;gap:12px}
.contact-item svg{width:26px;height:26px}
.contact-sep{width:2px;height:38px;background:var(--red)}
.contact-item small{display:block;font-size:12px;color:#555;text-transform:uppercase}
.contact-item strong{display:block;font-size:20px;font-weight:500;color:var(--ink)}
.main-nav{position:absolute;top:86px;right:133px;display:flex;gap:49px;font-size:15px;font-weight:500;text-transform:uppercase}
.main-nav a{color:var(--ink);text-decoration:none}
.main-nav a.active{color:var(--red)}

/* hero */
.hero{position:absolute;top:125px;left:0;width:1200px;height:575px;background:linear-gradient(160deg,#2a5f93 0%,#4d82b4 40%,#9fb9d0 70%,#ccd6df 100%)}
.hero-title{position:absolute;left:135px;top:64px;color:var(--white);font-size:41px;line-height:45px;text-shadow:0 2px 6px rgba(0,0,0,.35)}
.hero .btn{position:absolute;left:135px;top:216px}
.dots{position:absolute;top:539px;left:562px;display:flex;gap:10px;align-items:center}
.dots i{width:6px;height:6px;border-radius:50%;background:var(--white);opacity:.8}
.dots i.on{width:10px;height:10px;background:var(--red);border:2px solid var(--white);opacity:1}

/* charters */
.section-title{position:absolute;left:0;width:1200px;text-align:center;font-size:26px}
.charters{position:absolute;top:816px;left:130px;display:flex;gap:20px}
.card{width:298px;height:524px;background:var(--white);box-shadow:0 2px 10px rgba(0,0,0,.08)}
.card .photo{height:204px}
.card-body{padding:30px 27px 0}
.card h3{font-size:15px;font-weight:500;line-height:21px;text-transform:uppercase;color:var(--ink);margin-bottom:16px}
.card h3 span{color:var(--red)}
.card p{font-size:12.4px;line-height:18.3px}

/* split sections */
.split{position:absolute;left:0;width:1200px;display:flex}
.split-text{width:614px;position:relative}
.split .photo{width:586px}
.welcome{top:1391px;height:436px}
.welcome .split-text{background:var(--pink);padding:45px 70px 0 130px}
.welcome h2{font-size:30px;margin-bottom:22px}
.welcome p{font-size:14.2px;line-height:21px;color:#2a2a2a;margin-bottom:17px}
.welcome .btn{margin-top:10px}
.machine{top:1827px;height:499px}
.machine .photo{width:614px}
.machine .split-text{width:586px;padding:50px 0 0 74px}
.machine h2{font-size:28px;margin-bottom:20px}
.spec-list{list-style:none;font-size:14.4px;color:#2a2a2a}
.spec-list li{display:flex;align-items:center;gap:12px;height:30.5px}
.spec-list li::before{content:"";border-left:6px solid var(--red);border-top:5px solid transparent;border-bottom:5px solid transparent}
.machine p{font-size:15.5px;line-height:23px;color:#2a2a2a;margin:14px 0 28px}

/* features */
.features{position:absolute;top:2326px;left:0;width:1200px;height:612px;background:var(--pink)}
.scallop{position:absolute;left:0;top:2930px;width:1200px;height:16px}
.feature-row{position:absolute;top:67px;left:130px;display:flex;gap:41px}
.feature{width:284px;text-align:center}
.feature .photo{width:284px;height:284px;border-radius:50%}
.feature h3{font-size:23px;margin:40px 0 8px}
.feature p{font-size:15.2px;line-height:23px;color:#333;padding:0 14px;margin-bottom:22px}

/* blog */
.blog{position:absolute;top:3073px;left:131px;display:flex;gap:26px}
.post{width:296px}
.post .photo{height:207px}
.post h3{font-size:13px;margin:28px 0 12px}
.post p{font-size:12.4px;line-height:18.3px;margin-bottom:18px}

/* footer */
.site-footer{position:absolute;top:3577px;left:0;width:1200px;height:357px;background:var(--black);color:var(--white)}
.footer-brand{position:absolute;left:130px;top:96px;display:flex;align-items:center;gap:14px;font-size:44px;font-weight:500;color:var(--white)}
.footer-brand .brand-dot{width:36px;height:36px}
.footer-col{position:absolute;top:54px}
.footer-col h4{font-size:12.5px;font-weight:500;text-transform:uppercase;letter-spacing:.5px;margin-bottom:22px}
.footer-menu{list-style:none;font-size:11.5px;line-height:19.5px;text-transform:uppercase}
.footer-list{list-style:none}
.footer-list li{display:flex;align-items:center;gap:12px;font-size:11.5px;line-height:14px;height:50px}
.footer-list .icon{width:24px;height:24px;border-radius:50%;background:var(--white);flex:none;display:flex;align-items:center;justify-content:center}
.footer-list .icon svg{width:13px;height:13px}
.footer-rule{position:absolute;left:130px;top:273px;width:937px;height:1px;background:#2a2a2a}
.copyright{position:absolute;top:313px;left:0;width:1200px;text-align:center;font-size:10px}
</style>
</head>
<body>

<header class="site-header">
  <div class="brand"><span class="brand-dot"></span>Sun Keel</div>
  <div class="contact-bar">
    <div class="contact-item">
      <svg viewBox="0 0 26 26" fill="none" stroke="#e4132f" stroke-width="1.8"><rect x="3" y="6" width="20" height="14"/><path d="M3 6l10 8 10-8"/></svg>
      <span class="contact-sep"></span>
      <div><small>Email</small><strong>sunkeel.com</strong></div>
    </div>
    <div class="contact-item">
      <svg viewBox="0 0 26 26" fill="none" stroke="#e4132f" stroke-width="1.8"><path d="M7 3l4 5-2 3c1 3 3 5 6 6l3-2 5 4-2 3C13 22 4 13 4 5z"/></svg>
      <span class="contact-sep"></span>
      <div><small>Tel</small><strong>6104410</strong></div>
    </div>
  </div>
  <nav class="main-nav">
    <a class="active" href="#">Home</a><a href="#">About Us</a><a href="#">Services</a><a href="#">Blog</a><a href="#">Contact Us</a>
  </nav>
</header>

<section class="hero" role="img" aria-label="Photo of an angler on a boat holding a large tuna above the open sea">
  <h1 class="hero-title heading">Fishing, Spearfishing &amp;<br>Snorkeling Private<br>Charters</h1>
  <a class="btn btn-lg" href="#">Read More</a>
  <div class="dots"><i></i><i></i><i class="on"></i><i></i><i></i></div>
</section>

<h2 class="section-title heading" style="top:748px">Just bring your appetite for adventure</h2>
<div class="charters">
  <article class="card">
    <div class="photo" role="img" aria-label="Photo of a fisherman on a boat holding a tuna" style="background:linear-gradient(180deg,#4a82c4,#7fa6c8 55%,#5b6e5a)"></div>
    <div class="card-body">
      <h3>Fishing Private Charters:<br>From <span>US$1.000</span></h3>
      <p>Our Fishing Charters are all Offshore Trips. Depending on your choice we can offer a variety of fishing options. For the experienced angler, test your skills by casting lures or if you're just a beginner bottom fishing baits is always a good way to go. We specialise in putting you on big fish and will do what it takes to make sure you get a chance to experience what drag screaming is all about. Maximum 6 guests (4 anglers).</p>
    </div>
  </article>
  <article class="card">
    <div class="photo" role="img" aria-label="Underwater photo of a spearfisher with a mahi-mahi" style="background:radial-gradient(circle at 50% 55%,#3fa06a,#1a55b8 55%,#0c2f8a)"></div>
    <div class="card-body">
      <h3>Spearfishing Private<br>Charters: From <span>US$1.400</span></h3>
      <p>We welcome all experience levels and you will be accompanied by a safe diver in the water at all times to help you with anything&nbsp; you need! You are welcome to take along your equipment, however we provide the best equipment in the market. Our&nbsp; fishing grounds are all offshore so our Spearfishing Charters are all full day (minimum 8 hours). Maximum of 6 guests (4 divers)</p>
    </div>
  </article>
  <article class="card">
    <div class="photo" role="img" aria-label="Underwater photo of snorkelers among a school of fish" style="background:linear-gradient(180deg,#a9c4e6,#7d93c9 60%,#6a7fb8)"></div>
    <div class="card-body">
      <h3>Snorkelling Private<br>Charters: <span>US$1.200</span></h3>
      <p>We offer snorkelling trips to the Hole Chan Marine Reserve, to Shark Ray Alley, Coral Gardens, all destinations inside the barrier reef and in calm waters. But we also offer snorkelling trips to the offshore Atolls: Turneffe North or South, Half Moon Caye National&nbsp; Park and the Blue Hole. Our Snorkelling Trips are full day (minimum 8 hours). Maximum 6 guests.</p>
    </div>
  </article>
</div>

<section class="split welcome">
  <div class="split-text">
    <h2 class="heading">Welcome to Sun Keel</h2>
    <p>Sun Keel offers Fishing , Spearfishing and&nbsp; Snorkeling private charters in North Belize, Turneffe, Lighthouse Reef and the&nbsp; Blue Hole. No need to board crowded boats. Choose your privacy and let us&nbsp; pamper you with our exclusive service.</p>
    <p>Whether it is Snorkelling for the family, Tuna for the experienced angler, or Deep Sea Spearfishing for the fight of a lifetime, you will surely be pleased. Not only do we offer a vast assortment of trips but our local guides will coach you through each fight to ensure you catch your desired Trophy Fish.</p>
    <a class="btn btn-lg" href="#">Read More</a>
  </div>
  <div class="photo" role="img" aria-label="Photo of anglers on a boat fighting a leaping marlin" style="background:linear-gradient(180deg,#2452a3,#1b3f8a 50%,#3a5fa0 80%,#c7c9c8)"></div>
</section>

<section class="split machine">
  <div class="photo" role="img" aria-label="Photo of the charter sport-fishing boat on dark water at dusk" style="background:linear-gradient(180deg,#4c7aa6,#2d5b86 45%,#1d3f60 70%,#16304c)"></div>
  <div class="split-text">
    <h2 class="heading">Our fishing machine</h2>
    <ul class="spec-list">
      <li>Halvard 290 Open</li>
      <li>LFT 31'10" ; Beam11'6"</li>
      <li>Draft.: 2'0" ; Weight.10,000</li>
      <li>Fuel: 302 gals.</li>
      <li>Water 55 gals.</li>
      <li>Engines: 2 x 350hp Inboard</li>
      <li>Cruise Speed 20kn</li>
    </ul>
    <p>We outfit our boat with the latest electronics,<br>up to date safety gear and finest equipment</p>
    <a class="btn btn-lg" href="#">Read More</a>
  </div>
</section>

<section class="features">
  <div class="feature-row">
    <div class="feature">
      <div class="photo" role="img" aria-label="Photo of two anglers holding a mahi-mahi" style="background:radial-gradient(circle at 50% 70%,#5e6a3a,#7da4c9 70%)"></div>
      <h3 class="heading">How to fish</h3>
      <p>Lorem Ipsum is simply dummy text of the printing and type setting industry.</p>
      <a class="btn btn-sm" href="#">Read More</a>
    </div>
    <div class="feature">
      <div class="photo" role="img" aria-label="Underwater photo of a diver with a speared fish" style="background:radial-gradient(circle at 50% 60%,#3d6f8f,#1d64b8 60%,#0f4ea6)"></div>
      <h3 class="heading">Fly fishing</h3>
      <p>Lorem Ipsum is simply dummy text of the printing and type setting industry.</p>
      <a class="btn btn-sm" href="#">Read More</a>
    </div>
    <div class="feature">
      <div class="photo" role="img" aria-label="Photo of a sport-fishing boat cruising at sea" style="background:linear-gradient(180deg,#9cb6cf,#5f88ad 40%,#2f5a86 70%,#23476d)"></div>
      <h3 class="heading">Get started boating</h3>
      <p>Lorem Ipsum is simply dummy text of the printing and type setting industry.</p>
      <a class="btn btn-sm" href="#">Read More</a>
    </div>
  </div>
</section>
<svg class="scallop" viewBox="0 0 1200 16" preserveAspectRatio="none" aria-hidden="true">
  <defs><pattern id="wave" width="24" height="16" patternUnits="userSpaceOnUse"><path d="M0 0h24v4a12 10 0 0 1-24 0z" fill="#fce8ea"/></pattern></defs>
  <rect width="1200" height="16" fill="url(#wave)"/>
</svg>

<h2 class="section-title heading" style="top:3000px">Latest blog</h2>
<div class="blog">
  <article class="post">
    <div class="photo" role="img" aria-label="Aerial photo of a blue hole in a turquoise reef" style="background:radial-gradient(circle at 35% 45%,#0a2d6b 15%,#1e6fb3 30%,#4fc1c9 55%,#2a7fb8 80%)"></div>
    <h3 class="heading">Lorem ipsum is simply dummy text</h3>
    <p>There are many variations of passages of Lorem Ipsum available, but the majority have suffered alteration in some form, by injected humour, or randomised words which don't look even slightly believable. If you are going to use a passage of Lorem Ipsum, you need to be sure</p>
    <a class="btn btn-sm" href="#">Read More</a>
  </article>
  <article class="post">
    <div class="photo" role="img" aria-label="Photo of an angler reeling in with a bent rod at sea" style="background:linear-gradient(180deg,#8fb0d4,#b9cde2 50%,#3f5f85 62%,#2c4a6e)"></div>
    <h3 class="heading">Lorem ipsum is simply dummy text</h3>
    <p>There are many variations of passages of Lorem Ipsum available, but the majority have suffered alteration in some form, by injected humour, or randomised words which don't look even slightly believable. If you are going to use a passage of Lorem Ipsum, you need to be sure</p>
    <a class="btn btn-sm" href="#">Read More</a>
  </article>
  <article class="post">
    <div class="photo" role="img" aria-label="Photo of a fishing reel on a boat with a marlin jumping behind" style="background:linear-gradient(180deg,#9ab6d6,#3e6aa8 35%,#2a5296 70%,#8d98a6)"></div>
    <h3 class="heading">Lorem ipsum is simply dummy text</h3>
    <p>There are many variations of passages of Lorem Ipsum available, but the majority have suffered alteration in some form, by injected humour, or randomised words which don't look even slightly believable. If you are going to use a passage of Lorem Ipsum, you need to be sure</p>
    <a class="btn btn-sm" href="#">Read More</a>
  </article>
</div>

<footer class="site-footer">
  <div class="footer-brand"><span class="brand-dot"></span>Sun Keel</div>
  <div class="footer-col" style="left:480px">
    <h4>Menu</h4>
    <ul class="footer-menu"><li>Home</li><li>About Us</li><li>Services</li><li>Blog</li><li>Contact Us</li></ul>
  </div>
  <div class="footer-col" style="left:670px">
    <h4>Contact Us</h4>
    <ul class="footer-list">
      <li><span class="icon"><svg viewBox="0 0 14 14"><path d="M7 1a4 4 0 0 0-4 4c0 3 4 8 4 8s4-5 4-8a4 4 0 0 0-4-4z" fill="#000"/><circle cx="7" cy="5" r="1.5" fill="#fff"/></svg></span><span>27 Harbour Lane<br>Corozal Bay, BZ 10230</span></li>
      <li><span class="icon"><svg viewBox="0 0 14 14"><path d="M3 1l2 3-1 1.5c.6 1.7 1.8 2.9 3.5 3.5L9 8l3 2-1 2.5C6 12 2 8 1.5 3z" fill="#000"/></svg></span><span>Call Us<br>501.555.0148</span></li>
      <li><span class="icon"><svg viewBox="0 0 14 14"><rect x="2" y="3.5" width="10" height="7" fill="#000"/><path d="M2 3.5l5 4 5-4" stroke="#fff" fill="none"/></svg></span><span>E mail Us<br>info@sunkeel.com</span></li>
    </ul>
  </div>
  <div class="footer-col" style="left:962px">
    <h4>Follow Us</h4>
    <ul class="footer-list">
      <li><span class="icon"></span><span>Like us on<br>SHOALBOOK</span></li>
      <li><span class="icon"></span><span>Follow us on<br>TIDECHAT</span></li>
      <li><span class="icon"></span><span>Follow us on<br>CREWLINK</span></li>
    </ul>
  </div>
  <div class="footer-rule"></div>
  <p class="copyright">Copyright © 2021 All Rights Reserved</p>
</footer>

</body>
</html>
```